new roofing company card

New primary business card for roofing company.

Industry/Entity Type

Residential roofing/Specializing in Asphalt and Standing seam metal roofing

Contact Information for Business Card

Phone number is: 484 672 1058 Email: support@fennridgeroofworks.com website: www.fennridgeroofworks.com

Colors
EB3D1F
EC4F4E
F09395
F8D3D4
FCEDEE

```html
<!DOCTYPE html>
<html lang="en">
<head>
<meta charset="utf-8">
<title>Fennridge Roofworks Business Card</title>
<link rel="stylesheet" href="https://fonts.googleapis.com/css2?family=Montserrat:wght@400;500;700&display=swap">
<style>
  :root {
    --stage: #3a3a3a;
    --card-black: #1d1d1f;
    --card-white: #ffffff;
    --brand-red: #c4302b;
    --ink-dark: #2a2a2a;
    --ink-soft: #3d3d3d;
    --on-dark: #ffffff;
  }
  * { box-sizing: border-box; margin: 0; padding: 0; }
  html, body {
    width: 1200px; height: 875px; overflow: hidden;
    background: var(--stage);
    font-family: "Montserrat", Arial, sans-serif;
  }
  .canvas { position: relative; width: 1200px; height: 875px; }

  .card {
    position: absolute;
    width: 560px; height: 320px;
    border-radius: 18px;
    overflow: hidden;
    box-shadow: 0 14px 34px rgba(0,0,0,.35);
  }

  /* Back of card */
  .card-back {
    left: 60px; top: 110px;
    background: var(--card-black);
    display: flex; align-items: center; justify-content: center;
  }
  .wordmark { display: flex; align-items: center; gap: 12px; }
  .wordmark-square { width: 18px; height: 18px; background: var(--brand-red); flex: none; }
  .wordmark-name {
    font-weight: 700; font-size: 30px; letter-spacing: 1px;
    text-transform: uppercase; line-height: 1.05;
  }
  .card-back .wordmark-name { color: var(--on-dark); }

  /* Front of card */
  .card-front {
    left: 580px; top: 445px;
    background: var(--card-white);
  }
  .front-layout {
    position: absolute; inset: 0;
    display: flex; align-items: center;
    padding: 0 30px 40px 40px;
  }
  .front-brand { width: 230px; }
  .front-brand .wordmark-name { color: var(--ink-dark); font-size: 21px; }
  .front-brand .wordmark-square { width: 14px; height: 14px; }
  .divider {
    width: 2px; height: 150px; background: var(--brand-red);
    margin: 0 22px 0 14px; flex: none;
  }
  .contact-name { font-weight: 700; font-size: 22px; color: var(--ink-dark); }
  .contact-name .first { color: var(--brand-red); }
  .contact-title { font-size: 12px; color: var(--ink-soft); margin: 2px 0 14px; }
  .contact-list { list-style: none; }
  .contact-list li {
    display: flex; align-items: center; gap: 9px;
    font-size: 12px; color: var(--ink-dark); margin-bottom: 6px;
  }
  .contact-list svg { width: 12px; height: 12px; flex: none; }

  .front-bands { position: absolute; left: 0; bottom: 0; width: 560px; height: 60px; }
</style>
</head>
<body>
<main class="canvas">

  <section class="card card-back" aria-label="Card back">
    <div class="wordmark">
      <span class="wordmark-square"></span>
      <span class="wordmark-name">Fennridge<br>Roofworks</span>
    </div>
  </section>

  <section class="card card-front" aria-label="Card front">
    <div class="front-layout">
      <div class="front-brand">
        <div class="wordmark">
          <span class="wordmark-square"></span>
          <span class="wordmark-name">Fennridge<br>Roofworks</span>
        </div>
      </div>
      <div class="divider"></div>
      <div class="contact">
        <p class="contact-name"><span class="first">Tomas</span> Verell</p>
        <p class="contact-title">Managing Director</p>
        <ul class="contact-list">
          <li>
            <svg viewBox="0 0 12 12"><rect x="2.5" y="0.5" width="7" height="11" rx="1.5" fill="none" stroke="#c4302b" stroke-width="1.3"/><circle cx="6" cy="9.4" r=".8" fill="#c4302b"/></svg>
            484 672 1058
          </li>
          <li>
            <svg viewBox="0 0 12 12"><rect x="0.5" y="2" width="11" height="8" fill="#c4302b"/><path d="M0.8 2.4 6 6.6 11.2 2.4" fill="none" stroke="#fff" stroke-width="1"/></svg>
            support@fennridgeroofworks.com
          </li>
          <li>
            <svg viewBox="0 0 12 12"><circle cx="6" cy="6" r="5.4" fill="#c4302b"/><path d="M0.8 6h10.4M6 .6c-2.6 3-2.6 7.8 0 10.8M6 .6c2.6 3 2.6 7.8 0 10.8" fill="none" stroke="#fff" stroke-width=".8"/></svg>
            www.fennridgeroofworks.com
          </li>
        </ul>
      </div>
    </div>
    <svg class="front-bands" viewBox="0 0 560 60" aria-hidden="true">
      <polygon points="0,50 350,50 346,60 0,60" fill="#2a2a2a"/>
      <polygon points="360,12 560,12 560,60 342,60" fill="#c4302b"/>
      <polygon points="352,12 360,12 342,60 334,60" fill="#2a2a2a"/>
    </svg>
  </section>

</main>
</body>
</html>
```